Maple Hollow Bloom Panels Business card

Looking to have a business card design incorporating my logo for my flower wall business.

Industry/Entity Type

Wedding & event planning

Contact Information for Business Card

My business logo, my name - Lena Whitcombe (owner), my tagline - Let our blooms set your scene, phone # 401-726-3148, email address - maplehollowbloompanels@mailvane.net, my website - maplehollowbloompanels.net, Instagram handle- @maplehollowbloompanels, FB handle Handle - maplehollowbloompanels

Font styles to use
Other font styles liked:
• Sentaina is the font that is used in my logo

Requirements
Must have
• Would like a double sided business card

```html
<!DOCTYPE html>
<html lang="en">
<head>
<meta charset="utf-8">
<title>Maple Hollow Bloom Panels – Business Card</title>
<link rel="stylesheet" href="https://fonts.googleapis.com/css2?family=Roboto+Condensed:wght@400;700&display=swap">
<style>
  :root {
    --page-bg: #d9d4ce;
    --card-light: #ece6de;
    --card-dark: #2f2b2a;
    --seal-cream: #f3ebdf;
    --accent-pink: #c9939a;
    --text-light: #d6d0cb;
    --text-muted: #b9b2ad;
    --seal-ink: #2a2523;
    --seal-gold: #c9a65a;
  }
  * { box-sizing: border-box; margin: 0; padding: 0; }
  html, body {
    width: 1200px; height: 1200px; overflow: hidden;
    background: var(--page-bg);
    font-family: "Roboto Condensed", "Arial Narrow", sans-serif;
  }
  .business-card {
    position: absolute; left: 100px; top: 327px;
    width: 1000px; height: 545px;
    border-radius: 26px; overflow: hidden;
    background: var(--card-light);
    box-shadow: 0 10px 30px rgba(0,0,0,0.15);
  }
  .card-shapes { position: absolute; inset: 0; }
  .name-tab {
    position: absolute; left: 0; top: 72px;
    width: 20px; height: 34px;
    background: var(--accent-pink);
    border-radius: 0 6px 6px 0;
  }
  .owner-name {
    position: absolute; left: 55px; top: 68px;
    font-size: 32px; font-weight: 700; letter-spacing: 0.5px;
    color: var(--accent-pink);
  }
  .owner-role {
    position: absolute; left: 56px; top: 118px;
    font-size: 21px; color: var(--text-muted);
  }
  .contact-list {
    position: absolute; left: 55px; top: 202px;
    list-style: none;
  }
  .contact-item {
    display: flex; align-items: center; gap: 10px;
    height: 41px;
    font-size: 22px; color: var(--text-light);
  }
  .contact-icon { width: 20px; height: 20px; flex: none; fill: var(--text-muted); }
  .tagline {
    position: absolute; left: 48px; top: 452px;
    font-size: 23px; font-weight: 700;
    color: var(--accent-pink);
  }
  .brand-seal {
    position: absolute; left: 508px; top: 83px;
    width: 400px; height: 400px;
    display: flex; align-items: center; justify-content: center;
    text-align: center;
  }
  .brand-name {
    font-size: 44px; font-weight: 400; line-height: 1.15;
    color: var(--seal-ink);
  }
</style>
</head>
<body>
  <div class="business-card">
    <svg class="card-shapes" width="1000" height="545" viewBox="0 0 1000 545">
      <rect class="dark-panel" x="0" y="0" width="710" height="545" fill="var(--card-dark)"/>
      <rect class="light-panel" x="710" y="0" width="290" height="545" fill="var(--card-light)"/>
      <circle class="seal-backdrop" cx="710" cy="283" r="240" fill="var(--seal-cream)"/>
      <circle class="seal-ring" cx="708" cy="283" r="198" fill="none" stroke="var(--seal-gold)" stroke-width="2"/>
    </svg>

    <div class="name-tab"></div>
    <h1 class="owner-name">LENA WHITCOMBE</h1>
    <p class="owner-role">Owner</p>

    <ul class="contact-list">
      <li class="contact-item">
        <svg class="contact-icon" viewBox="0 0 24 24"><path d="M6.6 10.8a15.1 15.1 0 0 0 6.6 6.6l2.2-2.2c.3-.3.7-.4 1-.2 1.1.4 2.3.6 3.6.6.6 0 1 .4 1 1V20c0 .6-.4 1-1 1A17 17 0 0 1 3 4c0-.6.4-1 1-1h3.5c.6 0 1 .4 1 1 0 1.3.2 2.5.6 3.6.1.3 0 .7-.2 1z"/></svg>
        401-726-3148
      </li>
      <li class="contact-item">
        <svg class="contact-icon" viewBox="0 0 24 24"><path d="M3 6h18v12H3z M3 6l9 7 9-7" fill="var(--text-muted)" stroke="var(--card-dark)" stroke-width="1.6"/></svg>
        maplehollowbloompanels@mailvane.net
      </li>
      <li class="contact-item">
        <svg class="contact-icon" viewBox="0 0 24 24"><circle cx="12" cy="12" r="9"/><path d="M3 12h18M12 3c3 3 3 15 0 18M12 3c-3 3-3 15 0 18" fill="none" stroke="var(--card-dark)" stroke-width="1.4"/></svg>
        maplehollowbloompanels.net
      </li>
      <li class="contact-item">
        <svg class="contact-icon" viewBox="0 0 24 24"><circle cx="12" cy="12" r="8"/></svg>
        @maplehollowbloompanels
      </li>
      <li class="contact-item">
        <svg class="contact-icon" viewBox="0 0 24 24"><rect x="4" y="4" width="16" height="16" rx="2"/></svg>
        maplehollowbloompanels
      </li>
    </ul>

    <p class="tagline">Let our blooms set your scene</p>

    <div class="brand-seal">
      <p class="brand-name">Maple Hollow<br>Bloom Panels</p>
    </div>
  </div>
</body>
</html>
```